Business Card Design for Photographer

Updating business card design. Must use included logo. We're a luxury wedding photography business. Elegancy, luxury, consistency are messages we wish to convey.

Visit our website at www.colbyvarnway.com to familiarize yourself more with our brand design currently (fonts, colors etc.). This is what we want to maintain.

Target Market(s)

Luxury Brides and Grooms

Industry/Entity Type

Wedding

Contact Information for Business Card

Current logo (attached to brief)
Name: Colby Varnway
Phone: 5208813047
website/blog
Email

Requirements
Must have
• Current logo (attached to brief)
• Name: Colby Varnway
• Phone: 5208813047
• website/blog
• Email
• Instagram username
Should not have
• bright colors, fonts that don't suit our brand (visit www.colbyvarnway.com)

```html
<!DOCTYPE html>
<html lang="en">
<head>
<meta charset="utf-8">
<title>Colby Varnway Photographers – Business Card</title>
<link rel="stylesheet" href="https://fonts.googleapis.com/css2?family=Tenor+Sans&family=Allura&family=Lato:wght@300;400&display=swap">
<style>
  :root {
    --backdrop: #d9d9d9;
    --card: #ffffff;
    --ink: #5f6163;
    --ink-soft: #6c6e70;
    --band: #616366;
    --gold-light: #f3d77a;
    --gold-dark: #b8871f;
    --shadow: rgba(0, 0, 0, 0.22);
  }
  * { box-sizing: border-box; margin: 0; padding: 0; }
  html, body {
    width: 1200px;
    height: 852px;
    overflow: hidden;
    background: var(--backdrop);
  }
  .stage {
    position: relative;
    width: 1200px;
    height: 852px;
    display: flex;
    align-items: center;
    justify-content: center;
    gap: 60px;
  }
  .card {
    position: relative;
    width: 525px;
    height: 300px;
    background: var(--card);
    border-radius: 12px;
    box-shadow: 0 6px 14px var(--shadow);
    overflow: hidden;
  }

  /* Wordmark */
  .wordmark {
    display: flex;
    flex-direction: column;
    align-items: center;
    color: var(--ink);
    font-family: "Tenor Sans", sans-serif;
  }
  .wordmark__square {
    width: 74px;
    height: 74px;
    background: var(--ink);
    margin-bottom: 18px;
  }
  .wordmark__name {
    font-size: 30px;
    letter-spacing: 0.2em;
    line-height: 1;
    padding-left: 0.2em;
    text-transform: uppercase;
  }
  .wordmark__tag {
    margin-top: 10px;
    font-size: 12px;
    letter-spacing: 0.62em;
    padding-left: 0.62em;
    text-transform: uppercase;
  }

  /* Front */
  .card--front {
    display: flex;
    align-items: center;
    justify-content: center;
  }

  /* Back */
  .card__band {
    position: absolute;
    inset: 0;
    width: 100%;
    height: 100%;
  }
  .card--back .wordmark {
    position: absolute;
    top: 36px;
    left: 126px;
    width: 330px;
  }
  .card--back .wordmark__square {
    width: 44px;
    height: 44px;
    margin-bottom: 10px;
  }
  .card--back .wordmark__name { font-size: 19px; }
  .card--back .wordmark__tag { font-size: 8px; margin-top: 7px; }

  .contact {
    position: absolute;
    left: 136px;
    top: 168px;
    color: var(--ink-soft);
  }
  .contact__name {
    font-family: "Allura", cursive;
    font-size: 32px;
    line-height: 1;
    margin-bottom: 8px;
  }
  .contact__list {
    list-style: none;
    font-family: "Lato", sans-serif;
    font-weight: 400;
    font-size: 12.5px;
    line-height: 19px;
  }
  .contact__item {
    display: flex;
    align-items: center;
    gap: 10px;
  }
  .contact__icon {
    width: 11px;
    height: 11px;
    flex: none;
    fill: none;
    stroke: var(--ink-soft);
    stroke-width: 1.3;
  }
  .contact__icon--solid { fill: var(--ink-soft); stroke: none; }
</style>
</head>
<body>
<main class="stage">

  <section class="card card--front" aria-label="Card front">
    <div class="wordmark">
      <div class="wordmark__square"></div>
      <div class="wordmark__name">Colby Varnway</div>
      <div class="wordmark__tag">Photographers</div>
    </div>
  </section>

  <section class="card card--back" aria-label="Card back">
    <svg class="card__band" viewBox="0 0 525 300" preserveAspectRatio="none" aria-hidden="true">
      <defs>
        <linearGradient id="goldEdge" x1="0" y1="0" x2="0" y2="1">
          <stop offset="0" stop-color="var(--gold-light)"/>
          <stop offset="0.45" stop-color="var(--gold-dark)"/>
          <stop offset="0.75" stop-color="var(--gold-light)"/>
          <stop offset="1" stop-color="var(--gold-dark)"/>
        </linearGradient>
      </defs>
      <polygon points="0,0 92,0 100,300 0,300" fill="var(--band)"/>
      <polygon points="92,0 100,0 108,300 100,300" fill="url(#goldEdge)"/>
    </svg>

    <div class="wordmark">
      <div class="wordmark__square"></div>
      <div class="wordmark__name">Colby Varnway</div>
      <div class="wordmark__tag">Photographers</div>
    </div>

    <div class="contact">
      <p class="contact__name">Colby Varnway</p>
      <ul class="contact__list">
        <li class="contact__item">
          <svg class="contact__icon contact__icon--solid" viewBox="0 0 12 12" aria-hidden="true">
            <path d="M1 3.5C1 2 2 1 3 1h6c1 0 2 1 2 2.5L9 4.5V3.6H3v.9zM2.5 6 4 4.8h4L9.5 6v4.5h-7z"/>
          </svg>
          <span>(520) 881-3047</span>
        </li>
        <li class="contact__item">
          <svg class="contact__icon" viewBox="0 0 12 12" aria-hidden="true">
            <circle cx="6" cy="6" r="5"/><ellipse cx="6" cy="6" rx="2.2" ry="5"/><path d="M1 6h10"/>
          </svg>
          <span>www.colbyvarnway.com</span>
        </li>
        <li class="contact__item">
          <svg class="contact__icon" viewBox="0 0 12 12" aria-hidden="true">
            <rect x="1" y="2.5" width="10" height="7"/><path d="M1 2.5 6 6.5l5-4"/>
          </svg>
          <span>colby@colbyvarnway.com</span>
        </li>
        <li class="contact__item">
          <svg class="contact__icon" viewBox="0 0 12 12" aria-hidden="true">
            <circle cx="6" cy="6" r="4.6"/>
          </svg>
          <span>/colbyvarnwayphoto</span>
        </li>
      </ul>
    </div>
  </section>

</main>
</body>
</html>
```